Cd Cover Design needed for Electronic Music album

I need a cd cover design for my new album of Electronic music, sub-genre from Electronic to Techno to Tech-House to Dub-House.(just want people to Dance)
My artist name is "Velvet Circuitry" and the album is "Lantern of Drift". I have uploaded an image for artist name ,its just for the idea of how the letters go. Would like to see designs in blue was thinking of Audio equipment or audio wavs (looks like an earthquake meter) ,I am a fan of Masking images and puting another image inside, i would like the design to catch eyes and reach out for different and unique, my music ranges from soft to hard crunch within the same songs. I am excited to see what you come up with.
With many Thanks from Velvet Circuitry

I have uploaded 9 Design ideas,dont use the images i do not own them only downloaded, some of the images show the photoshop two image design.

the size and track names are below:

online distributor requires the size of 1448x1448
track font ,something straight and orderly (not to fancy for the lettering)
1. Meadow Vs Ironclad 6:54
2. Lantern of Drift 6:10
3. Z O Lively 8:04
4. Ever Roamin 7:04
5. Bound to wander 7:15
6. Fold into 5:40
7. Past the Lanterns gate 6:38

I would also like to have the designer(s) put on a small section on the inside cover designers contact info and type "designs by:" that way the designer gets some viewer coverage also.

Target Market(s)

Anyone that listens to Electronic / Techno / House / Dub.

Industry/Entity Type

Electronic

Colors
0455a3

Requirements
Must have
• The logo that I uploaded I was hoping that someone could design that better for me not using font style letters but drawn and put that together with the design. Please don't use my design that I uploaded (its not to appealing, its why im not a designer) ,its just to show how I want the letters. Also I like black as the background color.
Nice to have
• Image Masking ,like1, 2 or 3 images in one silhouette image, images done like from the album of Tinwharf except no squirrels ,Photoshop is a plus, really would like to see designs with real images that are masked with other images.

```html
<!DOCTYPE html>
<html lang="en">
<head>
<meta charset="utf-8">
<title>Velvet Circuitry – Lantern of Drift</title>
<link rel="stylesheet" href="https://fonts.googleapis.com/css2?family=Audiowide&display=swap">
<style>
  :root {
    --stage: #1c1c1e;
    --title-blue: #29b6ea;
    --subtitle-red: #e8284a;
    --sky-pale: #8fb4cc;
    --sky-mid: #3f6886;
    --sky-deep: #13263b;
    --road-dark: #0c141f;
    --trail-warm: #e8c596;
    --trail-hot: #fff1d8;
  }
  * { box-sizing: border-box; margin: 0; padding: 0; }
  html, body {
    width: 1200px;
    height: 900px;
    overflow: hidden;
    background: radial-gradient(ellipse at 50% 35%, #3a3a3d 0%, var(--stage) 70%);
  }
  .album-cover {
    position: absolute;
    left: 220px;
    top: 70px;
    width: 760px;
    height: 760px;
    overflow: hidden;
    box-shadow: 0 18px 50px rgba(0,0,0,0.6);
  }
  .cover-photo {
    position: absolute;
    inset: 0;
    background:
      radial-gradient(ellipse 55% 9% at 70% 20%, rgba(255,241,216,0.75), transparent 70%),
      radial-gradient(ellipse 60% 14% at 55% 56%, rgba(255,241,216,0.55), transparent 70%),
      radial-gradient(ellipse 75% 20% at 35% 70%, rgba(232,197,150,0.55), transparent 72%),
      radial-gradient(ellipse 60% 12% at 60% 88%, rgba(232,197,150,0.4), transparent 70%),
      linear-gradient(162deg,
        transparent 0%, transparent 38%,
        rgba(232,197,150,0.35) 48%, rgba(255,241,216,0.5) 55%,
        rgba(232,197,150,0.3) 63%, transparent 74%),
      linear-gradient(175deg,
        var(--sky-pale) 0%, var(--sky-mid) 14%, var(--sky-deep) 32%,
        #23384c 50%, #1a2736 72%, var(--road-dark) 100%);
  }
  .cover-text {
    position: absolute;
    inset: 0;
    font-family: "Audiowide", sans-serif;
    text-transform: uppercase;
  }
  .artist-name {
    position: absolute;
    left: 30px;
    top: 195px;
    font-size: 94px;
    font-weight: 400;
    line-height: 1.02;
    letter-spacing: 1px;
    color: var(--title-blue);
    text-shadow: 0 2px 10px rgba(0,0,0,0.35);
  }
  .album-title {
    position: absolute;
    left: 92px;
    top: 545px;
    font-size: 32px;
    letter-spacing: 1px;
    color: var(--subtitle-red);
  }
</style>
</head>
<body>
  <main class="album-cover">
    <div class="cover-photo" role="img" aria-label="Long-exposure night photo of a city road: blurred blue buildings above, bright warm light trails sweeping diagonally across the dark street"></div>
    <div class="cover-text">
      <h1 class="artist-name">Velvet<br>Circuitry</h1>
      <p class="album-title">Lantern of Drift</p>
    </div>
  </main>
</body>
</html>
```